Electrical & Communications Company Wordpress Themed Website Design

Hi everyone,

I need a wordpress themed website designed for a new company based in Sydney Australia called "TRELVEX". It delivers electrical and communication services to the domestic and commercial sectors.

It needs to be the FULL/COMPLETE wordpress theme! A clean and easy to use site.

Please guys take the time to look at these competitors sites:

www.quobble.com.au
www.zirconvoltworks.com.au
www.ubt.com.au
www.tallowwiring.com.au
www.wrightbergwire.com.au
www.gullivarwiremen.com.au

Please use these site for ideas only!!! we want to be original.

(If you would like to add electrical and communications to the logo that is O.K.)

Note: These logo's are registered trademarks of trelvex pty ltd.

Accreditation:

Bufo member (United cabling and signalling trades guild)

PLEASE CHECK THE WEB PLANNING LAYOUT BELOW FOR ROUGH IDEA

Have requested to increase payment to $400 and now guarantee payment!

Hi guys, forgot to mention i would like to see the business phone number prominently some where with a call to action.As we are a service business and need people to easly be able to see our contact number. Maybe top right courner but open to ideas. 

 Guys/Girls this is for a complete working word press theme that i can load up on the sever and access thru wordpress admin. Code etc

• - Logo Provided must be used
• - Themes and colours to be consisted with with brand
• - Fully customizable
• - Have a social share button from pinquo.com
• - Must be the full/complete theme for word press
• - zenpixbanks
• - contactform
• - would like orbe lumo charge bitfen displayed
• - Guarantee logo or something
• - Please don't waste your or our time submitting templates or copies of other sites original only!

```html
<!DOCTYPE html>
<html lang="en">
<head>
<meta charset="utf-8">
<title>TRELVEX — Electrical &amp; Communications</title>
<link rel="stylesheet" href="https://fonts.googleapis.com/css2?family=Open+Sans:wght@400;600;700&family=Titillium+Web:wght@300;400;600;700&family=Merriweather:wght@700&family=Exo:wght@500&display=swap">
<style>
:root{
  --red:#e3121b;
  --red-dark:#c30d14;
  --slate:#5b6a75;
  --slate-light:#7d8b95;
  --ink:#444;
  --body:#7a7a7a;
  --orange:#f07a00;
  --green:#6a9a12;
  --btn:#8fb8de;
  --panel:#f3f3f3;
  --line:#d9d9d9;
  --footer:#e4e4e4;
}
*{box-sizing:border-box;margin:0;padding:0}
html,body{width:1200px;height:1098px;overflow:hidden}
body{position:relative;background:#f4f4f4;font-family:"Open Sans",sans-serif;color:var(--body);font-size:11px}
.abs{position:absolute}
.top-band{left:0;top:0;width:1200px;height:110px;background:linear-gradient(#e5121b,#d90f17)}
.pylon-band{left:0;top:110px;width:1200px;height:295px;background:linear-gradient(#5d6c77,#6b7a85)}
.page{left:183px;top:18px;width:834px;height:838px;background:#fff;border-radius:6px;border:1px solid #e6e6e6}
.logo{left:195px;top:32px;display:flex;align-items:center;gap:8px}
.logo-dot{width:40px;height:40px;border-radius:50%;background:var(--red)}
.logo-name{font-family:"Titillium Web",sans-serif;font-weight:700;font-size:36px;color:#555;letter-spacing:1px;line-height:1}
.call{left:648px;top:22px;display:flex;align-items:center;gap:6px;font-family:"Titillium Web",sans-serif;font-weight:600;font-size:19px;color:#555}
.share{left:842px;top:16px;width:155px;height:41px;background:#fff;border-radius:0 0 5px 5px;box-shadow:0 2px 4px rgba(0,0,0,.2);display:flex;align-items:center;gap:5px;padding-left:16px;font-size:10px;color:#2f6db5}
.share .plus{width:12px;height:12px;background:#f26522;border-radius:2px}
.share .sq{width:12px;height:12px;background:#4a76b8;border-radius:2px}
.share .sep{color:#333;margin:0 3px}
.nav{left:579px;top:81px;display:flex;font-family:"Titillium Web",sans-serif;font-size:13px;color:#555}
.nav a{color:inherit;text-decoration:none;height:20px;line-height:20px;margin-right:28px}
.nav a.active{background:var(--red);color:#fff;border-radius:4px;padding:0 12px;margin-right:18px}
.hero{left:192px;top:111px;width:816px;height:293px;background:linear-gradient(90deg,#6d5a40 0%,#a08058 30%,#8d9aa3 60%,#6a7883 100%)}
.hero-cap{left:207px;top:351px;font-family:"Merriweather",serif;font-size:13px;color:#fff}
.dots{left:670px;top:381px;display:flex;gap:7px}
.dots span{width:14px;height:14px;border-radius:50%;background:#444;color:#fff;font-size:8px;text-align:center;line-height:14px}
.feature{left:766px;width:225px;height:77px;border-radius:5px;background:linear-gradient(#8a97a1,#6e7c87);border:1px solid #a9b3ba;display:flex;align-items:center;gap:20px;padding-left:18px;font-family:"Titillium Web",sans-serif;font-weight:300;font-size:19px;color:#fff;line-height:1.3}
.feature svg{flex:none}
h1.welcome{left:194px;top:420px;width:552px;font-size:19px;font-weight:700;color:var(--orange);border-bottom:1px solid var(--line);padding-bottom:2px;font-family:"Open Sans",sans-serif}
.intro{left:196px;top:450px;width:550px;line-height:20px;text-align:justify}
.intro p+p{margin-top:8px}
.testi-bar{left:196px;top:668px;width:550px;height:22px;background:linear-gradient(#f4f8fb,#dde7ee);font-weight:700;font-size:12px;color:#555;padding-left:58px;line-height:22px}
.pencil{left:206px;top:640px}
.quote{left:203px;width:536px;line-height:20px;color:#555}
.more{left:660px;width:80px;text-align:right;color:var(--green)}
.fade{height:23px;background:linear-gradient(#fff,#e8e8e8)}
.contact{left:764px;top:411px;width:243px;height:233px;background:linear-gradient(#fff 80%,#e9e9e9)}
.contact-head{height:40px;background:linear-gradient(#fff 0,#fff 18px,#5d6c77 18px,#4e5c66);color:#fff;font-weight:700;font-size:12px;padding:18px 0 0 62px;line-height:22px;position:relative}
.contact-head svg{position:absolute;left:8px;top:0}
.field{margin:12px 0 0 19px;color:#666}
.field .input{width:202px;height:16px;border:1px solid #ccc;margin-top:4px;background:#fff}
.btn{width:56px;height:19px;background:var(--btn);color:#fff;text-align:center;line-height:19px;border-radius:2px}
.search{left:764px;top:662px;width:241px;height:52px;background:var(--panel);border:1px solid #e2e2e2;border-radius:3px}
.blog{left:763px;top:733px;width:243px;height:110px;background:var(--panel);border:1px solid #e2e2e2;border-radius:3px}
.blog h3{font-family:"Exo",sans-serif;font-weight:500;font-size:14px;color:#444;position:absolute;left:54px;top:9px}
.blog strong{position:absolute;left:14px;top:36px;font-size:11px;color:#555;font-weight:600;letter-spacing:.3px}
.blog p{position:absolute;left:14px;top:55px;width:214px;line-height:15px;text-align:justify}
.footer{left:0;top:868px;width:1200px;height:230px;background:var(--footer)}
.foot-h{font-family:"Exo",sans-serif;font-weight:500;font-size:14px;color:#444}
.foot-links{left:186px;top:908px;line-height:16.7px;color:#2f5d96}
.foot-about{left:371px;top:914px;width:364px;line-height:20px;text-align:justify;color:#444}
.pay{left:782px;top:888px;width:235px;height:113px;background:#ececec;border:1px solid #d6d6d6;border-radius:3px}
.card{top:46px;width:59px;height:37px;border:1px solid #ccc;border-radius:3px;display:flex;align-items:center;justify-content:center;font-weight:700;font-size:11px;color:#fff}
.copy{left:0;top:1025px;width:1100px;text-align:center;line-height:17px;color:#555;font-size:11px}
</style>
</head>
<body>
<div class="abs top-band"></div>
<div class="abs pylon-band" role="img" aria-label="Faint pattern of electricity pylons on slate background"></div>
<div class="abs page"></div>

<div class="abs logo"><span class="logo-dot"></span><span class="logo-name">TRELVEX</span></div>

<div class="abs call">
  <svg width="24" height="32" viewBox="0 0 24 32"><path d="M5 2c3 0 4 6 2 8-1 1 2 9 5 11 2-1 6 1 6 4s-4 5-7 3C5 24 0 12 2 5c0-2 1-3 3-3z" fill="#d4141b"/><path d="M14 30h9" stroke="#999" stroke-width="2"/></svg>
  <span>1300-555-014</span>
</div>

<div class="abs share"><span class="plus"></span><span>Share</span><span class="sep">|</span><span class="sq"></span><span class="sq" style="background:#5a7cb0"></span><span class="sq" style="background:#6aa84f"></span><span class="sq" style="background:#3fa9d6"></span></div>

<nav class="abs nav"><a class="active" href="#">Home</a><a href="#">About Us</a><a href="#">Services</a><a href="#">Experience</a><a href="#">Quotes</a><a href="#">Contact</a></nav>

<div class="abs hero" role="img" aria-label="Modern home at dusk beside electricians working on a switchboard, with soft clouds"></div>
<div class="abs hero-cap">Lorem Ipsum is simply dummy text</div>
<div class="abs dots"><span>1</span><span>2</span><span>3</span></div>

<div class="abs feature" style="top:147px">
  <svg width="52" height="42" viewBox="0 0 52 42"><rect x="2" y="4" width="44" height="34" rx="3" fill="#eee"/><rect x="2" y="4" width="44" height="7" fill="#d55"/><circle cx="36" cy="28" r="12" fill="#fff" stroke="#333" stroke-width="2"/><path d="M36 20v8l5 3" stroke="#333" stroke-width="2" fill="none"/></svg>
  <span>24hours<br>7 days a week</span>
</div>
<div class="abs feature" style="top:234px">
  <svg width="52" height="52" viewBox="0 0 52 52"><circle cx="26" cy="26" r="24" fill="#c9d0d5"/><path d="M20 12c3 0 4 6 2 8-1 1 2 9 5 11 2-1 6 1 6 4s-4 4-7 3c-6-3-12-14-10-21 0-3 2-5 4-5z" fill="#fff"/></svg>
  <span>No Callout Fee</span>
</div>
<div class="abs feature" style="top:320px">
  <svg width="52" height="52" viewBox="0 0 52 52"><path d="M8 30 30 8h12v12L20 42z" fill="#eee" stroke="#bbb"/><circle cx="37" cy="13" r="3" fill="#888"/><circle cx="22" cy="28" r="7" fill="#2a83c6"/></svg>
  <span>Fixed Pricing</span>
</div>

<h1 class="abs welcome">Welcome To.....</h1>
<div class="abs intro">
  <p>Lorem Ipsum is simply dummy text of the printing and typesetting industry. Lorem Ipsum has been the industry's standard dummy text ever since the 1500s, when an unknown printer took a galley of type and scrambled it to make a type specimen book. It has survived not only five centuries, but also the leap into electronic typesetting, remaining essentially unchanged. It was popularised in the 1960s with the release of Dravenlet sheets containing Lorem Ipsum passages, and more recently with desktop publishing software like Quillset Pagecraft including versions of Lorem Ipsum.</p>
  <p>It is a long established fact that a reader will be distracted by the readable content of a page when looking at its layout. The point of using Lorem Ipsum is that it has a more-or-less normal distribution of letters, as opposed to using 'Content here, content here', accident, sometimes on purpose</p>
</div>

<div class="abs testi-bar">Testamonial</div>
<svg class="abs pencil" width="30" height="50" viewBox="0 0 30 50"><path d="M8 4l12 0 0 34-6 10-6-10z" fill="#6cb33f"/><rect x="8" y="2" width="12" height="6" fill="#f2c230"/></svg>
<p class="abs quote" style="top:708px">"Lorem Ipsum is simply dummy text of the printing and typesetting industry. Lorem Ipsum has been the industry's standard dummy text ever since the 1500s, when an unknown</p>
<div class="abs more" style="top:750px">read more...</div>
<p class="abs quote" style="top:770px">"Lorem Ipsum is simply dummy text of the printing and typesetting industry. Lorem Ipsum has been the industry's standard dummy text ever since the 1500s,</p>
<div class="abs more" style="top:802px">read more...</div>
<div class="abs fade" style="left:194px;top:820px;width:552px"></div>

<form class="abs contact">
  <div class="contact-head"><svg width="50" height="40" viewBox="0 0 50 40"><path d="M4 8 44 2 40 30 8 34z" fill="#29a3d6"/><path d="M4 8 26 20 44 2" stroke="#1b7fae" stroke-width="2" fill="none"/></svg>Contact Us Now</div>
  <div class="field">Enter your name:<div class="input"></div></div>
  <div class="field">Enter your email address:<div class="input"></div></div>
  <div class="field">Enter your contact number:<div class="input"></div></div>
  <div class="btn" style="margin:14px 0 0 162px">Send</div>
</form>

<div class="abs search">
  <svg class="abs" style="left:8px;top:10px" width="32" height="32" viewBox="0 0 32 32"><circle cx="13" cy="13" r="9" fill="#fff" stroke="#888" stroke-width="3"/><path d="M20 20l9 9" stroke="#555" stroke-width="4"/></svg>
  <div class="abs" style="left:36px;top:17px;width:120px;height:16px;border:1px solid #ccc;background:#fff"></div>
  <div class="abs btn" style="left:161px;top:16px">Send</div>
</div>

<div class="abs blog">
  <svg class="abs" style="left:8px;top:4px" width="38" height="36" viewBox="0 0 38 36"><rect x="4" y="4" width="30" height="26" fill="#e8e8e8" stroke="#999"/><path d="M9 12h20M9 17h20M9 22h14" stroke="#999" stroke-width="2"/><rect x="8" y="28" width="4" height="8" fill="#f2c230"/><rect x="26" y="28" width="4" height="8" fill="#f2c230"/></svg>
  <h3>New Post Blog</h3>
  <strong>Lorem Ipsum is simply dummy text</strong>
  <p>Lorem Ipsum is simply dummy text of inting and typesetting industry.</p>
</div>

<div class="abs footer"></div>
<h2 class="abs foot-h" style="left:183px;top:888px">More Information</h2>
<div class="abs foot-links">Home<br>About Us<br>Services<br>Experience<br>Quotes<br>Contact</div>
<h2 class="abs foot-h" style="left:370px;top:888px;width:366px;border-bottom:1px solid #d0d0d0;padding-bottom:2px">About Us</h2>
<p class="abs foot-about">Lorem Ipsum is simply dummy text of the printing and typesetting industry. Lorem Ipsum has been the industry's standard dummy text ever since the 1500s, when an unknown printer took a galley of type and scrambled it to make a type specimen book.</p>
<div class="abs pay">
  <h2 class="abs foot-h" style="left:16px;top:8px">We Accept payment</h2>
  <div class="abs card" style="left:16px;background:#fbe7a6;color:#1d3f7a">bitfen</div>
  <div class="abs card" style="left:88px;background:#1d3f7a">lumo charge</div>
  <div class="abs card" style="left:159px;background:#fff;color:#1d3f7a">orbe</div>
</div>
<div class="abs" style="left:0;top:1016px;width:1200px;border-top:1px solid #d0d0d0"></div>
<div class="abs copy">© 2010 trelvex - All Rights Reserved.<br>Need help? Mail us: info@trelvex.com&nbsp;&nbsp;Tel: 1-555-018-2290</div>
</body>
</html>
```